Design some Business Cards for MPLX

Wording for business cards:

Company: Harbor Vessel Brokers Alliance
Name: Dominic Farrow
Job Title: Network Development Executive
email: dominic@[login to view URL]
Tel/Mob: Mobile: +001 418-275-9062
Skype: [login to view URL]
Address: 4780 SE 63rd Blvd; Ste 240, Miami FL 33058, USA
website: [login to view URL]

```html
<!DOCTYPE html>
<html lang="en">
<head>
<meta charset="utf-8">
<title>HARVEL Business Cards</title>
<link href="https://fonts.googleapis.com/css2?family=Lato:wght@400;700&family=Montserrat:wght@500;700&display=swap" rel="stylesheet">
<style>
  :root {
    --page: #e9e9ee;
    --navy: #2e2a8f;
    --blue: #3b33b0;
    --blue-light: #5650c8;
    --red: #e0312f;
    --ink: #2a2a3a;
    --white: #ffffff;
  }
  * { margin: 0; padding: 0; box-sizing: border-box; }
  html, body { width: 1200px; height: 912px; overflow: hidden; }
  body {
    background: var(--page);
    font-family: "Lato", sans-serif;
    position: relative;
  }
  .card {
    position: absolute;
    width: 560px;
    height: 320px;
    border-radius: 6px;
    box-shadow: 0 10px 24px rgba(0,0,0,.18);
    overflow: hidden;
  }
  /* Front */
  .card-front { left: 320px; top: 90px; background: var(--white); color: var(--ink); }
  .brand { position: absolute; left: 36px; top: 70px; display: flex; align-items: center; gap: 12px; }
  .brand-dot { width: 46px; height: 46px; border-radius: 50%; background: var(--navy); flex: none; }
  .brand-name { font-family: "Montserrat", sans-serif; font-weight: 700; font-size: 38px; letter-spacing: 2px; color: var(--navy); line-height: 1; }
  .brand-tagline { position: absolute; left: 36px; top: 126px; font-family: "Montserrat", sans-serif; font-weight: 500; font-size: 9px; letter-spacing: 1px; text-transform: uppercase; color: var(--navy); }
  .holder { position: absolute; right: 30px; top: 40px; width: 250px; }
  .holder-name { font-family: "Montserrat", sans-serif; font-weight: 700; font-size: 19px; letter-spacing: 1px; text-transform: uppercase; color: var(--ink); }
  .holder-title { font-size: 10px; font-weight: 700; letter-spacing: .6px; text-transform: uppercase; color: var(--red); margin-top: 3px; }
  .holder-rule { height: 2px; background: var(--navy); margin-top: 6px; }
  .contact { list-style: none; font-size: 12px; color: var(--ink); }
  .contact li { display: flex; align-items: center; gap: 9px; margin-bottom: 8px; }
  .icon { width: 18px; height: 18px; flex: none; }
  .contact-phone { position: absolute; left: 310px; top: 116px; }
  .divider { position: absolute; left: 0; right: 30px; top: 182px; height: 2px; background: var(--navy); }
  .contact-web { position: absolute; left: 36px; top: 202px; }
  .bottom-rule { position: absolute; left: 36px; right: 30px; top: 290px; height: 2px; background: var(--navy); }
  /* Back */
  .card-back {
    left: 320px; top: 500px;
    background: linear-gradient(135deg, var(--blue-light) 0%, var(--blue) 55%, var(--navy) 100%);
    color: var(--white);
  }
  .card-back .lines { position: absolute; inset: 0; }
  .back-brand { position: absolute; left: 0; right: 0; top: 110px; display: flex; justify-content: center; align-items: center; gap: 14px; }
  .back-brand .brand-dot { background: var(--white); width: 50px; height: 50px; }
  .back-brand .brand-name { color: var(--white); font-size: 44px; }
  .back-tagline { position: absolute; left: 0; right: 0; top: 166px; text-align: center; font-family: "Montserrat", sans-serif; font-weight: 500; font-size: 10px; letter-spacing: 1.4px; text-transform: uppercase; }
  .back-web { position: absolute; left: 0; right: 0; top: 226px; text-align: center; font-size: 13px; letter-spacing: 2px; }
</style>
</head>
<body>

<section class="card card-front" aria-label="Business card front">
  <div class="brand">
    <span class="brand-dot"></span>
    <span class="brand-name">HARVEL</span>
  </div>
  <div class="brand-tagline">Harbor Vessel Brokers Alliance</div>

  <div class="holder">
    <div class="holder-name">Dominic Farrow</div>
    <div class="holder-title">Network Development Executive</div>
    <div class="holder-rule"></div>
  </div>

  <ul class="contact contact-phone">
    <li>
      <svg class="icon" viewBox="0 0 18 18"><circle cx="9" cy="9" r="9" fill="#2e2a8f"/><rect x="6" y="4" width="6" height="10" rx="1.2" fill="none" stroke="#fff" stroke-width="1.3"/><circle cx="9" cy="12" r=".8" fill="#fff"/></svg>
      +001 418-275-9062
    </li>
    <li>
      <svg class="icon" viewBox="0 0 18 18"><circle cx="9" cy="9" r="9" fill="#2e2a8f"/><circle cx="9" cy="9" r="3.5" fill="none" stroke="#fff" stroke-width="1.3"/></svg>
      DominicFarrow
    </li>
  </ul>

  <div class="divider"></div>

  <ul class="contact contact-web">
    <li>
      <svg class="icon" viewBox="0 0 18 18"><circle cx="9" cy="9" r="9" fill="#2e2a8f"/><rect x="4.5" y="6" width="9" height="6.5" fill="none" stroke="#fff" stroke-width="1.2"/><path d="M4.5 6l4.5 3.6L13.5 6" fill="none" stroke="#fff" stroke-width="1.2"/></svg>
      dominic@harborvb.com
    </li>
    <li>
      <svg class="icon" viewBox="0 0 18 18"><circle cx="9" cy="9" r="9" fill="#2e2a8f"/><circle cx="9" cy="9" r="4.5" fill="none" stroke="#fff" stroke-width="1.2"/><path d="M4.5 9h9M9 4.5c-2 2.5-2 6.5 0 9M9 4.5c2 2.5 2 6.5 0 9" fill="none" stroke="#fff" stroke-width="1"/></svg>
      www.harborvb.com
    </li>
    <li>
      <svg class="icon" viewBox="0 0 18 18"><circle cx="9" cy="9" r="9" fill="#2e2a8f"/><path d="M9 14s-3.5-3.6-3.5-6a3.5 3.5 0 0 1 7 0c0 2.4-3.5 6-3.5 6z" fill="none" stroke="#fff" stroke-width="1.2"/><circle cx="9" cy="8" r="1.1" fill="#fff"/></svg>
      4780 SE 63rd Blvd; Ste 240, Miami FL 33058, USA
    </li>
  </ul>

  <div class="bottom-rule"></div>
</section>

<section class="card card-back" aria-label="Business card back">
  <svg class="lines" viewBox="0 0 560 320" preserveAspectRatio="none">
    <line x1="0" y1="125" x2="560" y2="55" stroke="#e0312f" stroke-width="2"/>
    <line x1="0" y1="226" x2="560" y2="166" stroke="#e0312f" stroke-width="2"/>
  </svg>
  <div class="back-brand">
    <span class="brand-dot"></span>
    <span class="brand-name">HARVEL</span>
  </div>
  <div class="back-tagline">Harbor Vessel Brokers Alliance</div>
  <div class="back-web">www.harborvb.com</div>
</section>

</body>
</html>
```